Business Card Design

I am a new realtor. To stand out from the other 25 realtors in my firm I need a card that will stand out. I am the youngest realtor here, so I want something to reflect that. Something different, as opposed to the same old traditional, boring cards everyone else has. It of course needs to have my picture which I will download for you ( I included a black and white option as well as color. Either are fine) and you can crop it or do whatever you need to make it look the best. Our company colors are red and white. These don't have to be the only colors on the card, but the red especially needs to be a focal color. I like a clean, stream-line look while still eye-catching. Not over the top busy.
While I do have to provide the company logo, I am a contractor. Therefore, I want the focus on me and my information.
Industry/Entity Type
Realtor
Contact Information for Business Card
Marissa Dunholt
Realtor (this needs the realtor logo which has the R in the circle at the end)
(office)555.318.4620
(cell) 555.742.9037
Mdunholt@brv-homesale.example
It will also need our company logo which I will download and send
Requirements
Nice to have
- I like the look of the foil or metallic. However, this is definitely not a requirement

```html
<!DOCTYPE html>
<html lang="en">
<head>
<meta charset="utf-8">
<title>Marissa Dunholt – Realtor Business Card</title>
<link rel="stylesheet" href="https://fonts.googleapis.com/css2?family=Roboto+Condensed:wght@400;700&display=swap">
<style>
  :root {
    --brand-red: #cc1f24;
    --brand-red-deep: #9e1419;
    --brand-red-dark: #7d0f13;
    --paper: #f7f5ef;
    --white: #ffffff;
    --stage: #e9e6e1;
    --photo-light: #e8dcd6;
    --photo-mid: #8e7f79;
    --photo-dark: #3a302d;
  }
  * { box-sizing: border-box; margin: 0; padding: 0; }
  html, body { width: 1200px; height: 918px; overflow: hidden; }
  body { background: var(--stage); position: relative; font-family: "Roboto Condensed", Arial, sans-serif; }

  .card { position: absolute; left: 250px; width: 700px; height: 400px; overflow: hidden; box-shadow: 0 6px 18px rgba(0,0,0,.18); }
  .card--front { top: 39px; background: var(--brand-red); }
  .card--back { top: 479px; background: var(--paper); }

  /* Front */
  .front-shapes { position: absolute; inset: 0; }
  .house-sketch { position: absolute; left: 30px; top: 105px; width: 210px; height: 170px;
    background: linear-gradient(135deg, rgba(255,255,255,.08), rgba(120,10,14,.18)); border-radius: 4px; }
  .firm-name { position: absolute; left: 36px; top: 34px; display: flex; align-items: center; gap: 10px;
    color: var(--white); font-weight: 400; font-size: 20px; }
  .firm-name-square { width: 12px; height: 12px; background: var(--white); }
  .agent-name { position: absolute; left: 218px; top: 118px; width: 260px; text-align: right;
    color: var(--white); font-weight: 700; font-size: 38px; letter-spacing: -.5px; white-space: nowrap; }
  .agent-title { position: absolute; left: 228px; top: 168px; width: 250px; height: 26px;
    background: var(--white); color: var(--brand-red); font-weight: 700; font-size: 21px;
    text-align: right; padding-right: 10px; line-height: 26px; }
  .contact { position: absolute; left: 262px; top: 208px; color: var(--white); font-size: 23px; }
  .contact-line { display: flex; align-items: center; gap: 12px; height: 34px; }
  .contact-line svg { width: 22px; height: 22px; }
  .contact-email { position: absolute; left: 166px; top: 290px; width: 310px; text-align: right;
    color: var(--white); font-size: 19px; white-space: nowrap; }
  .agent-photo { position: absolute; inset: 0; }

  /* Back */
  .childs-drawing { position: absolute; inset: 0;
    background: radial-gradient(ellipse at 70% 30%, rgba(245,225,150,.45), transparent 55%),
                radial-gradient(ellipse at 20% 25%, rgba(170,200,230,.4), transparent 50%),
                radial-gradient(ellipse at 85% 80%, rgba(170,210,150,.4), transparent 45%),
                linear-gradient(180deg, var(--paper), #eef0e6); }
  .back-firm-name { position: absolute; left: 0; right: 0; top: 178px; display: flex; justify-content: center;
    align-items: center; gap: 14px; color: var(--brand-red); font-weight: 700; font-size: 40px; }
  .back-firm-square { width: 22px; height: 22px; background: var(--brand-red); }
</style>
</head>
<body>

<section class="card card--front">
  <svg class="front-shapes" viewBox="0 0 700 400" aria-hidden="true">
    <polygon points="470,0 560,0 490,400 400,400" fill="var(--brand-red-deep)"/>
    <polygon points="400,90 480,40 455,200" fill="var(--brand-red-dark)"/>
  </svg>
  <div class="house-sketch" role="img" aria-label="Faint pencil sketch of a house"></div>
  <div class="firm-name"><span class="firm-name-square"></span>Marlowe Reed &amp; Company</div>

  <h1 class="agent-name">Marissa Dunholt</h1>
  <div class="agent-title">Realtor</div>

  <div class="contact">
    <div class="contact-line">
      <svg viewBox="0 0 24 24" aria-hidden="true"><rect x="3" y="4" width="18" height="16" rx="2" fill="none" stroke="#fff" stroke-width="2"/><rect x="6" y="7" width="12" height="4" fill="#fff"/><circle cx="8" cy="15" r="1.3" fill="#fff"/><circle cx="12" cy="15" r="1.3" fill="#fff"/><circle cx="16" cy="15" r="1.3" fill="#fff"/></svg>
      <span>555.318.4620</span>
    </div>
    <div class="contact-line">
      <svg viewBox="0 0 24 24" aria-hidden="true"><rect x="6" y="2" width="12" height="20" rx="2" fill="none" stroke="#fff" stroke-width="2"/><circle cx="12" cy="18" r="1.3" fill="#fff"/></svg>
      <span>555.742.9037</span>
    </div>
  </div>
  <div class="contact-email">Mdunholt@brv-homesale.example</div>

  <svg class="agent-photo" viewBox="0 0 700 400" role="img" aria-label="Black and white portrait photo of the realtor">
    <defs>
      <linearGradient id="photoTone" x1="0" y1="0" x2="0" y2="1">
        <stop offset="0" stop-color="var(--photo-light)"/>
        <stop offset=".55" stop-color="var(--photo-mid)"/>
        <stop offset="1" stop-color="var(--photo-dark)"/>
      </linearGradient>
    </defs>
    <polygon points="560,0 700,0 700,400 490,400" fill="url(#photoTone)"/>
  </svg>
</section>

<section class="card card--back">
  <div class="childs-drawing" role="img" aria-label="Soft crayon drawing of a house, sun, tree and family"></div>
  <div class="back-firm-name"><span class="back-firm-square"></span>Marlowe Reed &amp; Company</div>
</section>

</body>
</html>
```